CM Candle Tube Packaging Design

Website: www.corvelmarin.example
IG: @corvel.marin
Tagline: Elevate Your Ambiance
My brand is a sophisticated brand with luxury candles made of coconut wax. Im looking for an upscale minimalist chic design.
Discover the transformative power of positive energy with Corvel Marin candles. Indulge in true luxury with our specially crafted coconut wax blend that not only ignites captivating scents but also embodies modern elegance and empowering elements.
At Corvel Marin we're committed to delivering a unique and exhilarating aromatic experience to all candle lovers. Each candle is meticulously handcrafted in small batches using luxury fragrance oils exclusively formulated for coconut wax.
Our candles are:
Clean-burning
Paraben-Free
Phthalate-Free
Skin-Safe
Pet-Friendly
Look and feel

```html
<!DOCTYPE html>
<html lang="en">
<head>
<meta charset="utf-8">
<title>Corvel Marin – Candle Tube Labels</title>
<link rel="stylesheet" href="https://fonts.googleapis.com/css2?family=Noto+Serif:ital,wght@0,400;1,400&family=Oswald:wght@500&display=swap">
<style>
  :root {
    --bg: #e4e4e4;
    --leaf-light: #c2f5a8;
    --leaf-mid: #8fd68a;
    --leaf-deep: #3e8a78;
    --band: #2b2d30;
    --band-edge: #111214;
    --accent: #a9ee96;
    --ink-light: #e6e6e6;
    --ink-dark: #1a1a1a;
  }
  * { margin: 0; padding: 0; box-sizing: border-box; }
  html, body { width: 1200px; height: 873px; overflow: hidden; background: var(--bg); }
  .canvas { position: relative; width: 1200px; height: 873px; }

  .tube-label { position: absolute; width: 231px; height: 444px; overflow: hidden; border-radius: 4px; }
  .tube-label--circle { left: 333px; top: 166px; }
  .tube-label--plain  { left: 636px; top: 314px; }

  .leaf-pattern {
    position: absolute; inset: 0;
    background:
      radial-gradient(ellipse 60% 40% at 30% 20%, rgba(62,138,120,.55), transparent 70%),
      radial-gradient(ellipse 40% 60% at 85% 75%, rgba(62,138,120,.5), transparent 70%),
      linear-gradient(150deg, var(--leaf-deep) 0%, var(--leaf-mid) 35%, var(--leaf-light) 60%, var(--leaf-mid) 100%);
  }
  .lid-seam { position: absolute; left: 0; right: 0; height: 2px; background: rgba(30,60,50,.35); }

  .info-band {
    position: absolute; left: 0; right: 0; bottom: 0;
    background: linear-gradient(90deg, var(--band) 0%, var(--band) 55%, var(--band-edge) 100%);
    text-align: center;
  }
  .tube-label--circle .info-band { top: 250px; }
  .tube-label--plain .info-band { top: 297px; }

  .tagline {
    font-family: "Noto Serif", serif; font-style: italic; font-size: 12.5px;
    letter-spacing: 1.1px; color: var(--accent);
  }
  .tube-label--plain .tagline { color: var(--ink-light); }
  .story {
    font-family: "Noto Serif", serif; font-style: italic; font-size: 5.6px;
    line-height: 6.8px; letter-spacing: .7px; color: var(--ink-light);
    width: 184px; margin: 3px auto 0;
  }
  .benefits { display: flex; justify-content: center; gap: 6px; }
  .benefit { width: 36px; display: flex; flex-direction: column; align-items: center; gap: 3px; }
  .benefit svg { width: 15px; height: 15px; }
  .benefit span {
    font-family: "Oswald", sans-serif; font-weight: 500; font-size: 5.4px;
    white-space: nowrap; color: var(--accent);
  }
  .tube-label--plain .benefit span { color: var(--ink-light); }

  .brand-seal {
    position: absolute; left: 52px; top: 188px; width: 124px; height: 124px;
    border-radius: 50%; background: var(--band);
    border: 1.5px solid var(--ink-light); box-shadow: inset 0 0 0 5px var(--band);
    display: flex; align-items: center; justify-content: center;
  }
  .brand-name {
    font-family: "Noto Serif", serif; font-weight: 400; text-align: center;
    line-height: 1.05; letter-spacing: 1px;
  }
  .brand-seal .brand-name { color: var(--accent); font-size: 19px; }
  .brand-mark {
    position: absolute; left: 88px; top: 168px; width: 130px;
  }
  .brand-mark .brand-name { color: var(--ink-dark); font-size: 22px; text-align: right; }
</style>
</head>
<body>
<main class="canvas">

  <section class="tube-label tube-label--circle">
    <div class="leaf-pattern" role="img" aria-label="Stylised green leaf and branch pattern"></div>
    <div class="lid-seam" style="top:117px"></div>
    <div class="info-band">
      <p class="tagline" style="margin-top:76px">Elevate Your Ambiance</p>
      <p class="story">Discover the transformative power of positive energy with Corvel Marin candles. Indulge in true luxury with our specially crafted coconut wax blend that not only ignites captivating scents but also embodies modern elegance and empowering elements.</p>
      <div class="benefits" style="margin-top:12px">
        <div class="benefit"><svg viewBox="0 0 16 16"><circle cx="8" cy="8" r="7" fill="none" stroke="#e6e6e6"/><path d="M8 3.5c2 2.5 3 4 3 5.5a3 3 0 0 1-6 0c0-1.5 1-3 3-5.5z" fill="none" stroke="#e6e6e6"/></svg><span>Clean-burning</span></div>
        <div class="benefit"><svg viewBox="0 0 16 16"><circle cx="8" cy="8" r="7" fill="#e6e6e6"/><path d="M5 11c0-4 3-6 6-6 0 4-2 6-6 6z" fill="#2b2d30"/></svg><span>Paraben-Free</span></div>
        <div class="benefit"><svg viewBox="0 0 16 16"><circle cx="8" cy="8" r="7" fill="none" stroke="#e6e6e6"/><path d="M6.5 4h3M7 4v3l-2 4.5h6L9 7V4" fill="none" stroke="#e6e6e6"/></svg><span>Phthalate-Free</span></div>
        <div class="benefit"><svg viewBox="0 0 16 16"><circle cx="8" cy="8" r="7" fill="none" stroke="#e6e6e6"/><path d="M5 9.5l2 2 4-5" fill="none" stroke="#e6e6e6"/></svg><span>Skin-Safe</span></div>
        <div class="benefit"><svg viewBox="0 0 16 16"><circle cx="8" cy="8" r="7" fill="#e6e6e6"/><path d="M8 12s-3.5-2.2-3.5-4.4A1.8 1.8 0 0 1 8 6.6a1.8 1.8 0 0 1 3.5 1C11.5 9.8 8 12 8 12z" fill="#2b2d30"/></svg><span>Pet-Friendly</span></div>
      </div>
    </div>
    <div class="brand-seal"><p class="brand-name">CORVEL<br>MARIN</p></div>
  </section>

  <section class="tube-label tube-label--plain">
    <div class="leaf-pattern" role="img" aria-label="Stylised green leaf and branch pattern"></div>
    <div class="lid-seam" style="top:116px"></div>
    <div class="brand-mark"><p class="brand-name">CORVEL<br>MARIN</p></div>
    <div class="info-band">
      <p class="tagline" style="margin-top:6px">Elevate Your Ambiance</p>
      <p class="story" style="margin-top:6px">Discover the transformative power of positive energy with Corvel Marin candles. Indulge in true luxury with our specially crafted coconut wax blend that not only ignites captivating scents but also embodies modern elegance and empowering elements.</p>
      <div class="benefits" style="margin-top:12px">
        <div class="benefit"><svg viewBox="0 0 16 16"><circle cx="8" cy="8" r="7" fill="none" stroke="#e6e6e6"/><path d="M8 3.5c2 2.5 3 4 3 5.5a3 3 0 0 1-6 0c0-1.5 1-3 3-5.5z" fill="none" stroke="#e6e6e6"/></svg><span>Clean-burning</span></div>
        <div class="benefit"><svg viewBox="0 0 16 16"><circle cx="8" cy="8" r="7" fill="#e6e6e6"/><path d="M5 11c0-4 3-6 6-6 0 4-2 6-6 6z" fill="#2b2d30"/></svg><span>Paraben-Free</span></div>
        <div class="benefit"><svg viewBox="0 0 16 16"><circle cx="8" cy="8" r="7" fill="none" stroke="#e6e6e6"/><path d="M6.5 4h3M7 4v3l-2 4.5h6L9 7V4" fill="none" stroke="#e6e6e6"/></svg><span>Phthalate-Free</span></div>
        <div class="benefit"><svg viewBox="0 0 16 16"><circle cx="8" cy="8" r="7" fill="none" stroke="#e6e6e6"/><path d="M5 9.5l2 2 4-5" fill="none" stroke="#e6e6e6"/></svg><span>Skin-Safe</span></div>
        <div class="benefit"><svg viewBox="0 0 16 16"><circle cx="8" cy="8" r="7" fill="#e6e6e6"/><path d="M8 12s-3.5-2.2-3.5-4.4A1.8 1.8 0 0 1 8 6.6a1.8 1.8 0 0 1 3.5 1C11.5 9.8 8 12 8 12z" fill="#2b2d30"/></svg><span>Pet-Friendly</span></div>
      </div>
    </div>
  </section>

</main>
</body>
</html>
```